New Townhome community needs for sale sign.

need a 4 foot by 8 foot banner to put on building listing newly constructed townhomes as "coming soon" to market. Construction is scheduled to be completed Dec 2024. Sale of units will begin Spring of 2025.
6 individual townhome units each 2,000 square feet. each unit is 3 bedroom 2.5 bathroom with 2 car garage and each has a rooftop "sky lounge" with amazing views. Gated community. Units available for sale Spring of 2025. Real estate company selling units will be KLM & Partners. Will need KLM & Partners Logo on the banner. Would like to keep with the same blue color scheme as the KLM & Partners logo. phone number on banner to be 602-555-4179. web klmpartnersx.com.

```html
<!DOCTYPE html>
<html lang="en">
<head>
<meta charset="utf-8">
<title>KLM &amp; Partners – Townhomes Coming Soon Banner</title>
<link rel="stylesheet" href="https://fonts.googleapis.com/css2?family=Source+Sans+3:wght@400;600;700&family=Oswald:wght@600&display=swap">
<style>
  :root {
    --page: #ffffff;
    --card: #e3f3fa;
    --panel-a: #d3e7f4;
    --panel-b: #cfe0ee;
    --navy: #1c6d9b;
    --sky: #22a7d9;
    --ink: #333333;
    --white: #ffffff;
  }
  * { margin: 0; padding: 0; box-sizing: border-box; }
  html, body {
    width: 1200px; height: 1000px; overflow: hidden;
    background: var(--page);
    font-family: "Source Sans 3", sans-serif;
  }
  .banner {
    position: absolute; left: 413px; top: 126px;
    width: 374px; height: 747px;
    background: var(--card);
    color: var(--navy);
    overflow: hidden;
  }
  .backdrop {
    position: absolute; left: 0; top: 0; width: 374px; height: 441px;
    background: linear-gradient(100deg, var(--panel-a) 0%, var(--panel-b) 40%, var(--panel-a) 70%, var(--card) 100%);
    opacity: 0.75;
  }
  .headline {
    position: absolute; left: 25px; top: 12px;
    font-size: 104px; font-weight: 400; line-height: 1; letter-spacing: -2px;
  }
  .ribbon { position: absolute; left: 239px; top: 0; width: 107px; height: 108px; }
  .ribbon-text {
    position: absolute; left: 239px; top: 28px; width: 107px;
    text-align: center; color: var(--white);
    font-size: 26px; line-height: 26px;
  }
  .title {
    position: absolute; left: 27px; top: 134px;
    font-family: "Oswald", sans-serif; font-weight: 600;
    font-size: 46px; line-height: 47px; color: var(--sky);
    letter-spacing: 0.5px; transform: scaleX(0.86); transform-origin: left;
  }
  .date-box {
    position: absolute; left: 230px; width: 116px; height: 123px;
    border: 1.5px solid var(--navy); text-align: center;
  }
  .date-box .label {
    background: var(--navy); color: var(--white);
    font-size: 18px; line-height: 20px;
  }
  .completion { top: 140px; }
  .completion .label { height: 47px; padding-top: 3px; }
  .completion .month { font-size: 23px; line-height: 26px; margin-top: 2px; }
  .completion .year { font-size: 50px; line-height: 44px; }
  .sales { top: 299px; }
  .sales .label { height: 29px; padding-top: 5px; }
  .sales .season { font-size: 34px; line-height: 40px; margin-top: 2px; }
  .sales .year { font-size: 50px; line-height: 46px; }
  .summary {
    position: absolute; left: 27px; top: 296px; width: 150px;
    font-size: 23px; line-height: 26px;
  }
  .features-bar {
    position: absolute; left: 28px; top: 451px; width: 318px; height: 35px;
    background: var(--navy);
  }
  .features-bar svg { position: absolute; left: 114px; top: 0; }
  .features-bar span {
    position: absolute; left: 9px; top: 1px;
    color: var(--white); font-size: 27px; line-height: 32px;
  }
  .feature-list { position: absolute; top: 501px; list-style: none; font-size: 17.5px; line-height: 21.7px; }
  .feature-list li { position: relative; padding-left: 15px; }
  .feature-list li::before {
    content: ""; position: absolute; left: 0; top: 9px;
    width: 4px; height: 4px; background: var(--sky);
  }
  .feature-list.col-a { left: 29px; }
  .feature-list.col-b { left: 170px; width: 180px; }
  .brand {
    position: absolute; left: 28px; top: 633px; width: 318px;
    display: flex; align-items: center; justify-content: center; gap: 10px;
  }
  .brand-mark { width: 26px; height: 26px; background: var(--navy); }
  .brand-name { font-size: 32px; font-weight: 600; color: var(--ink); letter-spacing: -0.5px; }
  .phone {
    position: absolute; left: 0; width: 374px; top: 683px; text-align: center;
    color: var(--ink); font-size: 30px; letter-spacing: 1.5px; line-height: 30px;
  }
  .web {
    position: absolute; left: 0; width: 374px; top: 715px; text-align: center;
    color: var(--ink); font-size: 20px; letter-spacing: 1.5px; line-height: 20px;
  }
</style>
</head>
<body>
  <main class="banner">
    <div class="backdrop" role="img" aria-label="Faint background of building window panes"></div>

    <h1 class="headline">Sale!</h1>

    <svg class="ribbon" viewBox="0 0 107 108" aria-hidden="true">
      <polygon points="0,0 107,0 107,82 53.5,108 0,82" fill="var(--navy)"/>
    </svg>
    <p class="ribbon-text">Coming<br>Soon</p>

    <h2 class="title">INDIVIDUAL<br>TOWNHOME<br>UNITS</h2>

    <section class="date-box completion">
      <p class="label">Construction<br>Completion</p>
      <p class="month">December</p>
      <p class="year">2024</p>
    </section>

    <p class="summary">6 individual townhome units each 2,000 square feet.</p>

    <section class="date-box sales">
      <p class="label">Sales Begin</p>
      <p class="season">Spring</p>
      <p class="year">2025</p>
    </section>

    <div class="features-bar">
      <span>Features</span>
      <svg width="24" height="35" viewBox="0 0 24 35" aria-hidden="true">
        <polyline points="2,0 20,17.5 2,35" fill="none" stroke="var(--card)" stroke-width="2"/>
      </svg>
    </div>

    <ul class="feature-list col-a">
      <li>3 bedrooms</li>
      <li>2.5 bathrooms</li>
      <li>2-car garage</li>
    </ul>
    <ul class="feature-list col-b">
      <li>Rooftop “sky lounge” with amazing views</li>
      <li>Gated community</li>
    </ul>

    <div class="brand">
      <span class="brand-mark" aria-hidden="true"></span>
      <span class="brand-name">KLM &amp; Partners</span>
    </div>

    <p class="phone">602-555-4179</p>
    <p class="web">www.klmpartnersx.com</p>
  </main>
</body>
</html>
```